Dog grooming business card
This is a business card for m dog grooming business like it say above.
In the priorities box below I will have the text that I want on the card.

Industry/Entity Type

Business

Colors

Designer to choose colors to be used in the design.

Requirements
Must have
• My logo and the insurance stamp must be on the card.

Text it must have :

Professional grooming services
Email: lindomerfield@brightmail.example
Text or call 1 705 318 6052
KSR certified/member
Pet first aid certified
Next appointment ___________________________________
Nice to have
• Greens to match my logo

```html
<!DOCTYPE html>
<html lang="en">
<head>
<meta charset="utf-8">
<title>Lindo Merfield – Grooming Business Card</title>
<link href="https://fonts.googleapis.com/css2?family=Libre+Baskerville:wght@400;700&display=swap" rel="stylesheet">
<style>
  :root {
    --backdrop: #e9e6e1;
    --card-white: #ffffff;
    --ink: #1f1d1e;
    --panel-black: #2a2728;
    --leaf-green: #9bc54f;
    --line-grey: #555555;
    --badge-blue: #3b6fb6;
  }
  * { margin: 0; padding: 0; box-sizing: border-box; }
  html, body {
    width: 1200px; height: 914px; overflow: hidden;
    background: var(--backdrop);
    font-family: "Libre Baskerville", Georgia, serif;
  }
  .canvas { position: relative; width: 1200px; height: 914px; }
  .card {
    position: absolute; left: 220px; width: 760px; height: 434px;
    background: var(--card-white); overflow: hidden;
    box-shadow: 0 6px 18px rgba(0,0,0,.18);
  }
  .card--front { top: 22px; }
  .card--back { top: 478px; }
  .card__diagonal { position: absolute; inset: 0; }
  .contact {
    position: absolute; left: 40px; top: 34px;
    color: var(--ink); font-size: 22px; line-height: 1.5;
  }
  .contact__line--center { padding-left: 70px; }
  .contact__appointment { font-size: 19px; padding-left: 10px; }
  .appointment-rule {
    width: 250px; border-bottom: 1.5px solid var(--line-grey);
    margin: 18px 0 0 0;
  }
  .insurance-badge {
    position: absolute; left: 30px; bottom: 46px;
    width: 78px; height: 36px; border-radius: 7px;
    background: var(--card-white); border: 2px solid var(--badge-blue);
  }
  .brand {
    position: absolute; display: flex; align-items: center; gap: 14px;
    font-weight: 700; font-size: 36px; white-space: nowrap;
  }
  .brand__dot { width: 40px; height: 40px; border-radius: 50%; }
  .brand--front { right: 50px; bottom: 70px; color: var(--leaf-green); }
  .brand--front .brand__dot { background: var(--leaf-green); }
  .brand--back-top { left: 120px; top: 110px; color: var(--leaf-green); }
  .brand--back-top .brand__dot { background: var(--leaf-green); }
  .brand--back-panel { right: 60px; bottom: 90px; color: var(--card-white); font-size: 30px; }
  .brand--back-panel .brand__dot { background: var(--card-white); }
</style>
</head>
<body>
<main class="canvas">

  <section class="card card--front" aria-label="Business card, contact side">
    <svg class="card__diagonal" width="760" height="434" viewBox="0 0 760 434" aria-hidden="true">
      <polygon points="170,434 760,18 760,434" fill="var(--leaf-green)"/>
      <polygon points="235,434 760,46 760,434" fill="var(--panel-black)"/>
    </svg>
    <div class="contact">
      <p class="contact__line">Professional grooming services</p>
      <p class="contact__line contact__line--center">1 705 318 6052</p>
      <p class="contact__line">lindomerfield@brightmail.example</p>
      <p class="contact__line">KSR certified/member</p>
      <p class="contact__line">Pet first aid certified</p>
      <p class="contact__appointment">Next appointment</p>
      <div class="appointment-rule"></div>
      <div class="appointment-rule"></div>
    </div>
    <div class="insurance-badge" role="img" aria-label="Insurance stamp"></div>
    <div class="brand brand--front"><span class="brand__dot"></span>Lindo Merfield</div>
  </section>

  <section class="card card--back" aria-label="Business card, brand side">
    <svg class="card__diagonal" width="760" height="434" viewBox="0 0 760 434" aria-hidden="true">
      <polygon points="130,434 760,160 760,434" fill="var(--leaf-green)"/>
      <polygon points="195,434 760,186 760,434" fill="var(--panel-black)"/>
    </svg>
    <div class="brand brand--back-top"><span class="brand__dot"></span>Lindo Merfield</div>
    <div class="brand brand--back-panel"><span class="brand__dot"></span>Lindo Merfield</div>
  </section>

</main>
</body>
</html>
```